Veteran Owned General Contractor needs Bold New Business Cards

We are a service disabled veteran owned small business. We're a general contractor that specializes in excavation, underground utilities, site work, land clearing and demolition. We would like a fresh, simple, bold, new look for our business cards. We're open to ideas! We'd like to incorporate the following information on the card:

Company Name & Logo, Name of Person, Job Title, Office Phone, Fax, Cell Phone, Email Address, Website, SDVOSB

Our logo is included. We look forward to your thoughts.

Thank you!
Updates

Reason: Hello Due to the overwhelming response to this project, we are extending the deadline one time to allow for improved communication and feedback with the top candidates. We would like to thank everyone for their hard work and exceptional creativity! Thank you

Industry/Entity Type

Business

Contact Information for Business Card

Font styles to use
Sans Serif

Requirements
Nice to have
• As we are a veteran owned company, it would be nice to incorporate an American flag into the design. Maybe on the back?

```html
<!DOCTYPE html>
<html lang="en">
<head>
<meta charset="utf-8">
<title>Ridgeford7 Inc – Business Card</title>
<link rel="stylesheet" href="https://fonts.googleapis.com/css2?family=Open+Sans:wght@400;700;800&display=swap">
<style>
  :root {
    --page-bg: #d8d5cf;
    --card-bg: #eef0ee;
    --brand-green: #4c9a2a;
    --deep-green: #3f8a22;
    --swoosh-black: #161616;
    --text-grey: #595959;
    --text-dark: #1e1e1e;
    --mark-dark: #3a3d3f;
  }
  * { margin: 0; padding: 0; box-sizing: border-box; }
  html, body { width: 1200px; height: 969px; overflow: hidden; }
  body {
    background: var(--page-bg);
    font-family: "Open Sans", Arial, sans-serif;
    position: relative;
  }
  .business-card {
    position: absolute;
    left: 100px;
    top: 200px;
    width: 1000px;
    height: 569px;
    background: var(--card-bg);
    border-radius: 34px;
    overflow: hidden;
    box-shadow: 0 12px 34px rgba(0,0,0,0.18);
  }
  .card-swoosh {
    position: absolute;
    inset: 0;
    width: 100%;
    height: 100%;
  }
  .brand-square {
    position: absolute;
    left: 198px;
    top: 69px;
    width: 66px;
    height: 66px;
    border-radius: 10px;
    background: var(--mark-dark);
  }
  .brand-name {
    position: absolute;
    left: 52px;
    top: 186px;
    font-weight: 800;
    font-size: 44px;
    letter-spacing: 1px;
    color: var(--brand-green);
    line-height: 1;
  }
  .person {
    position: absolute;
    right: 126px;
    top: 196px;
    text-align: right;
  }
  .person-name {
    font-weight: 700;
    font-size: 31px;
    color: var(--brand-green);
    line-height: 1.2;
  }
  .person-title {
    font-weight: 400;
    font-size: 24px;
    color: var(--text-dark);
    margin-top: 6px;
    line-height: 1.2;
  }
  .contact-list {
    position: absolute;
    left: 52px;
    top: 334px;
    list-style: none;
  }
  .contact-item {
    display: flex;
    align-items: center;
    height: 39px;
    font-size: 24px;
    color: var(--text-grey);
  }
  .contact-icon {
    width: 24px;
    height: 24px;
    margin-right: 14px;
    fill: var(--deep-green);
    flex: none;
  }
</style>
</head>
<body>
  <div class="business-card">
    <svg class="card-swoosh" viewBox="0 0 580 330" preserveAspectRatio="none" aria-hidden="true">
      <path d="M465 0 L580 0 L580 330 L330 330 C440 300 522 205 522 120 C522 62 498 22 465 0 Z" fill="var(--brand-green)"/>
      <path d="M300 330 C430 302 512 222 534 130 C536 215 478 290 402 330 Z" fill="var(--swoosh-black)"/>
      <path d="M402 330 C478 290 536 215 534 130" fill="none" stroke="#ffffff" stroke-width="2"/>
    </svg>

    <div class="brand-square"></div>
    <div class="brand-name">RIDGEFORD7 INC</div>

    <div class="person">
      <div class="person-name">DALE TURNER</div>
      <div class="person-title">CEO/ FOUNDER</div>
    </div>

    <ul class="contact-list">
      <li class="contact-item">
        <svg class="contact-icon" viewBox="0 0 24 24"><path d="M6.6 10.8a15.1 15.1 0 0 0 6.6 6.6l2.2-2.2a1 1 0 0 1 1-.25 11.4 11.4 0 0 0 3.6.57 1 1 0 0 1 1 1V20a1 1 0 0 1-1 1A17 17 0 0 1 3 4a1 1 0 0 1 1-1h3.5a1 1 0 0 1 1 1c0 1.25.2 2.45.57 3.57a1 1 0 0 1-.25 1z"/></svg>
        512 384 7720
      </li>
      <li class="contact-item">
        <svg class="contact-icon" viewBox="0 0 24 24"><path d="M7 1h10a2 2 0 0 1 2 2v18a2 2 0 0 1-2 2H7a2 2 0 0 1-2-2V3a2 2 0 0 1 2-2zm0 3v14h10V4zm5 15.5a1.2 1.2 0 1 0 0 2.4 1.2 1.2 0 0 0 0-2.4z"/></svg>
        512 906 4418
      </li>
      <li class="contact-item">
        <svg class="contact-icon" viewBox="0 0 24 24"><path d="M6 2h12v5H6zM3 8h18a2 2 0 0 1 2 2v7h-4v5H5v-5H1v-7a2 2 0 0 1 2-2zm4 8v4h10v-4z"/></svg>
        512 384 7731
      </li>
      <li class="contact-item">
        <svg class="contact-icon" viewBox="0 0 24 24"><path d="M2 5h20v2l-10 6L2 7zm0 4.3 10 6 10-6V19H2z"/></svg>
        dale@ridgeford7.com
      </li>
      <li class="contact-item">
        <svg class="contact-icon" viewBox="0 0 24 24"><path d="M12 1a11 11 0 1 0 0 22 11 11 0 0 0 0-22zm-1 19.9A9 9 0 0 1 4.2 9.4L9 14v1a2 2 0 0 0 2 2zm6.9-2.6A2 2 0 0 0 16 17h-1v-3a1 1 0 0 0-1-1H8v-2h2a1 1 0 0 0 1-1V8h2a2 2 0 0 0 2-2v-.4a9 9 0 0 1 2.9 12.7z"/></svg>
        www.ridgeford7.com
      </li>
    </ul>
  </div>
</body>
</html>
```